LETTERHEAD & ENVELOPE: eye-catching stationary design for our custom office furniture business

Our company recently rebranded and we are in need of new stationary. Specifically, we need branded letterhead for standard paper size (8.5” x 11”), and matching envelopes, size: #9.

All designs should incorporate our brand colors, brand typeface, and logo. Please view attached brand guidelines document for brand colors, and brand description.

Letterhead: 8.5” x 11” Must include CedarlineKTV Logo, Talbot Greaves Certified Dealer Logo, mailing address, phone number, website, and email address.

Envelope: 9.5” x 4.125” Must include CedarlineKTV Logo, mailing address, and Talbot Greaves Certified Dealer Logo.

Attached files include:

```html
<!DOCTYPE html>
<html lang="en">
<head>
<meta charset="utf-8">
<title>CedarlineKTV Stationery</title>
<link href="https://fonts.googleapis.com/css2?family=Raleway:wght@300&family=Roboto:wght@300;400&display=swap" rel="stylesheet">
<style>
  :root {
    --backdrop: #8c8c8c;
    --paper: #f5f5f5;
    --envelope: #f1f1f1;
    --flap: #ececed;
    --brand-green: #5d7f72;
    --ink: #5a5a5a;
    --dealer-red: #e8402a;
    --watermark: #e2e6e4;
  }
  * { margin: 0; padding: 0; box-sizing: border-box; }
  html, body { width: 1200px; height: 947px; overflow: hidden; }
  body { background: var(--backdrop); position: relative; font-family: "Roboto", sans-serif; }

  .sheet { position: absolute; background: var(--paper); overflow: hidden; }
  .letterhead { left: 121px; top: 121px; width: 484px; height: 684px; }
  .envelope-back { left: 626px; top: 350px; width: 434px; height: 216px; background: var(--envelope); }
  .envelope-front { left: 626px; top: 588px; width: 434px; height: 217px; background: var(--envelope); }

  .brand { position: absolute; display: flex; align-items: center; }
  .brand-dot { border-radius: 50%; background: var(--brand-green); flex: none; }
  .brand-name { font-family: "Raleway", sans-serif; font-weight: 300; color: var(--brand-green); line-height: 1; }

  .letterhead .brand { left: 37px; top: 171px; top: 50px; gap: 8px; }
  .letterhead .brand-dot { width: 26px; height: 26px; }
  .letterhead .brand-name { font-size: 21px; }

  .contact { position: absolute; left: 341px; top: 40px; list-style: none; font-size: 6.8px; color: var(--ink); letter-spacing: 0.1px; }
  .contact li { display: flex; align-items: flex-start; gap: 5px; line-height: 9.2px; margin-bottom: 1.5px; }
  .contact svg { width: 6px; height: 6px; flex: none; margin-top: 1.5px; fill: var(--brand-green); }

  .dealer { position: absolute; display: flex; align-items: center; }
  .dealer-dot { border-radius: 50%; background: var(--dealer-red); flex: none; }
  .dealer-name { color: var(--dealer-red); font-weight: 300; white-space: nowrap; }
  .letterhead .dealer { left: 37px; top: 628px; gap: 6px; }
  .letterhead .dealer-dot { width: 20px; height: 20px; }
  .letterhead .dealer-name { font-size: 9px; }

  .watermark { position: absolute; border-radius: 50%; background: var(--watermark); }
  .letterhead .watermark { left: 242px; top: 470px; width: 270px; height: 270px; }
  .envelope-front .watermark { left: 279px; top: 77px; width: 170px; height: 170px; }

  .flap { position: absolute; left: 0; top: 0; width: 434px; height: 70px; }
  .envelope-back .brand-dot { position: absolute; left: 204px; top: 21px; width: 24px; height: 24px; }

  .envelope-front .brand { left: 28px; top: 26px; gap: 7px; }
  .envelope-front .brand-dot { width: 20px; height: 20px; }
  .envelope-front .brand-name { font-size: 16px; }
  .return-address { position: absolute; left: 55px; top: 48px; font-size: 5.6px; line-height: 7.8px; color: var(--ink); }
  .envelope-front .dealer { left: 27px; top: 177px; gap: 5px; }
  .envelope-front .dealer-dot { width: 15px; height: 15px; }
  .envelope-front .dealer-name { font-size: 7px; }
</style>
</head>
<body>
  <section class="sheet letterhead" aria-label="Letterhead">
    <div class="watermark"></div>
    <div class="brand">
      <span class="brand-dot"></span>
      <span class="brand-name">CedarlineKTV</span>
    </div>
    <ul class="contact">
      <li><svg viewBox="0 0 10 10"><path d="M5 0a3.6 3.6 0 0 0-3.6 3.6C1.4 6.3 5 10 5 10s3.6-3.7 3.6-6.4A3.6 3.6 0 0 0 5 0zm0 5a1.4 1.4 0 1 1 0-2.8A1.4 1.4 0 0 1 5 5z"/></svg><span>418 NE Alderbrook, Suite 150<br>Portland, OR 97210</span></li>
      <li><svg viewBox="0 0 10 10"><path d="M2 0.5l2 2.2-1 1.3c.6 1.3 1.7 2.4 3 3l1.3-1 2.2 2L8.6 9.7C4.5 9.5.5 5.5.3 1.4z"/></svg><span>503.555.0148</span></li>
      <li><svg viewBox="0 0 10 10"><path d="M0 2h10v6H0zM.8 2.6L5 5.6l4.2-3"/></svg><span>info@cedarlinektv.com</span></li>
      <li><svg viewBox="0 0 10 10"><circle cx="5" cy="5" r="4.6"/></svg><span>cedarlinektv.com</span></li>
    </ul>
    <div class="dealer">
      <span class="dealer-dot"></span>
      <span class="dealer-name">Talbot Greaves Certified Dealer</span>
    </div>
  </section>

  <section class="sheet envelope-back" aria-label="Envelope back">
    <svg class="flap" viewBox="0 0 434 70" aria-hidden="true">
      <path d="M1 0 L16 50 Q20 62 34 63 L410 61 Q422 60 424 48 L433 0 Z" fill="var(--flap)" stroke="#dcdcdc" stroke-width="0.8"/>
    </svg>
    <span class="brand-dot"></span>
  </section>

  <section class="sheet envelope-front" aria-label="Envelope front">
    <div class="watermark"></div>
    <div class="brand">
      <span class="brand-dot"></span>
      <span class="brand-name">CedarlineKTV</span>
    </div>
    <p class="return-address">418 NE Alderbrook, Suite 150<br>Portland, OR 97210</p>
    <div class="dealer">
      <span class="dealer-dot"></span>
      <span class="dealer-name">Talbot Greaves Certified Dealer</span>
    </div>
  </section>
</body>
</html>
```